Social Search engine to end child poverty

Velquor.org is a search engine based in Houston, that donates 50% or more of its profits to nonprofit organizations that focus on ending child poverty. We consider itself a social business, claims to support full financial transparency,protect the privacy of its users;

Velquor shows advertisements next to its search results, and is paid by partners every time a user is directed to an advertiser via a sponsored link.
We are committed to becoming a privacy friendly search engine. Searches will be encrypted, not stored permanently, and data will not not sold to third party advertisers.
Like www.parvink.org Every search done by website visitor will generate a TUPRAK that will be stored in his wallet. Then the visitor can donate these TUPRAKS to The idea behind is evry donation will put a SMILE back on a child face

The search engine will partner with foundations/associations/NGOs that will be able to propose crowdfunding campaigns on the landing page

The beta test will be done with african children. So the landing page should show faces of happiness, joy, children

Please find attached inspirational ideas in the PDF file

Target Market(s)

NGO, Foundation, association, donators based in USA

Industry/Entity Type

Charity

Number of Pages Required

5+ page

Colors
33a6d7
fbed22
f04a50
a54499
f78d1f
add136

Requirements
Must have
• Landing page
• 0- Number of TUPRAKS collected worlwide/number of projects funded
• 1- explaining how it works and
• 2- samples of fundable projects
• 3- Become partner
• Search results
• 1- Sponsored results should be differentiated
• 2- The search page should advertise initiative pr people that acts in the world to end child poverty.
• 3 It should also provide quizzes with some metrics/figures on child poverty
• Under the search engine bar should be "News" "Videos

```html
<!DOCTYPE html>
<html lang="en">
<head>
<meta charset="utf-8">
<title>Velquor.org — Give Meaning To Your Searches</title>
<link rel="stylesheet" href="https://fonts.googleapis.com/css2?family=Roboto:wght@400;500;700&family=Poppins:wght@400;500;600&display=swap">
<style>
:root{
  --red:#e8333f;
  --blue:#2e8ccd;
  --blue-dark:#1f6fae;
  --navy:#243a63;
  --ink:#1d1d25;
  --text:#555a66;
  --orange:#f47d20;
  --green:#a3c936;
  --health:#e8343c;
  --edu:#2e8fd0;
  --lavender:#f3f1f9;
  --white:#fff;
}
*{box-sizing:border-box;margin:0;padding:0}
html,body{width:1200px;height:5254px;overflow:hidden}
body{position:relative;font-family:"Poppins",sans-serif;color:var(--text);background:var(--white)}
.abs{position:absolute}
h1,h2,h3,h4{font-family:"Roboto",sans-serif;color:var(--ink)}
.btn{position:absolute;display:flex;align-items:center;justify-content:center;border-radius:22px;font-family:"Roboto",sans-serif;font-weight:700;color:var(--white);text-transform:uppercase;letter-spacing:.5px}
.btn-red{background:var(--red);box-shadow:0 4px 10px rgba(232,51,63,.35)}
.rule{position:absolute;height:4px;width:70px;background:var(--navy)}

/* hero */
.hero{left:0;top:0;width:1200px;height:788px;background:linear-gradient(180deg,#9cb3cf 0%,#8aa6c6 55%,#3b4f7a 100%)}
.hero-kids{left:0;top:440px;width:1200px;height:348px;background:linear-gradient(180deg,rgba(220,170,130,0) 0%,rgba(170,120,95,.55) 40%,rgba(60,70,110,.9) 100%)}
.brand{font-family:"Roboto",sans-serif;font-weight:700;color:var(--navy)}
.hero-title{left:0;width:1200px;top:132px;text-align:center;font-size:50px;font-weight:700;color:var(--navy)}
.hero-sub{left:0;width:1200px;top:198px;text-align:center;font-size:22px;line-height:32px;color:var(--navy)}
.hero-brand{left:0;width:1200px;top:258px;text-align:center;font-size:60px}
.search{position:absolute;background:var(--white);border-radius:26px;display:flex;align-items:center;padding:0 26px;font-size:14px;color:#444;box-shadow:0 3px 12px rgba(0,0,0,.12)}
.search svg{position:absolute;right:22px}
.menu span{display:block;width:32px;height:4px;background:var(--navy);margin-bottom:6px;border-radius:2px}

/* welcome */
.welcome-title{left:147px;top:893px;font-size:38px;font-weight:500}
.welcome-copy{left:147px;top:982px;width:386px;font-size:13px;line-height:24px}
.welcome-copy p+p{margin-top:8px}
.media{background:linear-gradient(135deg,#7ea6c9,#4d6f96 60%,#3b3f4e)}
.play{position:absolute;display:flex;align-items:center;gap:10px;color:var(--white);font-size:12px;line-height:15px;font-family:"Roboto",sans-serif}
.play i{width:32px;height:32px;border-radius:50%;background:var(--white);display:flex;align-items:center;justify-content:center}

/* how it works */
.how-title{left:0;width:1200px;top:1414px;text-align:center;font-size:38px;font-weight:500;color:var(--white)}
.step{position:absolute;top:1550px;width:284px;height:319px;background:var(--white);text-align:center;padding-top:26px}
.step .ico{width:98px;height:98px;border-radius:50%;background:var(--blue);margin:0 auto;display:flex;align-items:center;justify-content:center}
.step h3{margin-top:26px;font-size:17px;font-weight:500;letter-spacing:.3px}
.step p{margin:12px 24px 0;font-size:13px;line-height:22px;color:#444}
.joint{position:absolute;top:1680px;width:44px;height:44px;border-radius:50%;background:var(--white);border:3px solid var(--blue);display:flex;align-items:center;justify-content:center}

/* projects */
.sec-title{left:0;width:1200px;text-align:center;font-size:38px;font-weight:500}
.cat{position:absolute;top:2305px;width:228px;height:194px;display:flex;flex-direction:column;align-items:center;padding-top:32px;color:var(--white);font-family:"Roboto",sans-serif;font-weight:700;font-size:16px;letter-spacing:.5px}
.cat i{width:96px;height:96px;border-radius:50%;background:var(--white);display:flex;align-items:center;justify-content:center;margin-bottom:22px}
.card{position:absolute;width:288px;height:412px;background:var(--white);box-shadow:0 4px 14px rgba(0,0,0,.12)}
.card .photo{height:200px}
.card h3{text-align:center;margin-top:26px;font-size:18px;font-weight:500;letter-spacing:.5px}
.card p{text-align:center;margin:10px 22px 0;font-size:12px;line-height:21px;color:#555}
.card .foot{position:absolute;left:0;right:0;bottom:0;height:70px;border-top:1px solid #e6e6ea;display:flex;align-items:center;justify-content:space-between;padding:0 20px 0 28px}
.card .view{background:var(--navy);color:var(--white);font-family:"Roboto",sans-serif;font-weight:700;font-size:11px;border-radius:18px;padding:10px 22px;letter-spacing:.3px}
.card .price{color:var(--red);font-family:"Roboto",sans-serif;font-weight:700;font-size:20px}
.card .foot:after{content:"";position:absolute;left:190px;top:0;bottom:0;border-left:1px solid #e6e6ea}

/* news */
.news{position:absolute;left:604px;width:452px;height:182px;background:var(--white);border:1px solid #e3e1ea}
.news .photo{position:absolute;left:0;top:0;width:190px;height:100%}
.news h4{position:absolute;left:214px;top:26px;font-size:15px;font-weight:500;color:#222}
.news .meta{position:absolute;left:214px;top:62px;font-size:12px;color:var(--blue-dark);font-weight:600;display:flex;gap:16px}
.news p{position:absolute;left:214px;top:90px;width:220px;font-size:12px;line-height:21px;color:#555}

/* partners */
.partners{left:0;top:4315px;width:1200px;height:460px;background:var(--navy)}
.badge{position:absolute;width:170px;height:78px;background:var(--white);display:flex;align-items:center;justify-content:center}
.badge span{display:block;background:#c9ccd3;border-radius:4px}
.skyline{left:0;top:4764px;width:1200px;height:62px;background:linear-gradient(180deg,#2f4a7a,#4a6aa3)}

/* footer */
.foot-h{position:absolute;top:4896px;font-family:"Roboto",sans-serif;font-weight:700;font-size:17px;color:#222;letter-spacing:.5px}
.foot-p{position:absolute;font-size:12.5px;line-height:20px;color:#444}
.social{position:absolute;top:5036px;left:143px;display:flex;gap:8px}
.social i{width:32px;height:32px;border:1.5px solid #333;border-radius:50%}
.contact{position:absolute;left:500px;display:flex;gap:14px;font-size:13px;line-height:18px;color:#444}
.contact i{width:30px;height:30px;border:1.5px solid #333;border-radius:6px;display:flex;align-items:center;justify-content:center;flex:none}
.copy{left:0;top:5182px;width:1200px;height:72px;border-top:1px solid #e4e4e8;display:flex;align-items:center;justify-content:center;font-size:14px;color:#333}
</style>
</head>
<body>

<!-- HERO -->
<section class="abs hero" role="img" aria-label="Photo of a light blue painted brick wall behind the hero"></section>
<div class="abs hero-kids" role="img" aria-label="Photo of seven smiling children sitting in a row on the floor"></div>
<div class="abs brand" style="left:143px;top:38px;font-size:36px">Velquor.org</div>
<a class="btn btn-red" style="left:896px;top:44px;width:108px;height:38px;font-size:13px;font-weight:500">Donate</a>
<div class="abs menu" style="left:1024px;top:50px"><span></span><span></span><span></span></div>
<h1 class="abs hero-title">Give Meaning To Your Searches</h1>
<p class="abs hero-sub">With Velquor, your searches funds programs targeting<br>disadvantaged children</p>
<div class="abs brand hero-brand">Velquor.org</div>
<div class="search" style="left:310px;top:347px;width:580px;height:52px">Your search goes here...
  <svg width="26" height="26" viewBox="0 0 26 26"><circle cx="11" cy="11" r="8" fill="none" stroke="var(--blue)" stroke-width="3"/><path d="M17 17l7 7" stroke="var(--navy)" stroke-width="3.5" stroke-linecap="round"/></svg>
</div>

<!-- WELCOME -->
<h2 class="abs welcome-title">Welcome to Velquor</h2>
<div class="rule" style="left:147px;top:955px"></div>
<div class="abs welcome-copy">
  <p>Sed ut perspiciatis unde omnis iste natus error sit voluptatem accusantium doloremque laudantium, totam rem aperiam, eaque ipsa quae ab illo inventore veritatis et quasi architecto beatae vitae dicta sunt explicabo. Nemo</p>
  <p>Nemo enim ipsam voluptatem quia voluptas sit aspernatur aut odit aut fugit, sed quia consequuntur magni dolores eos qui ratione voluptatem sequi nesciunt.</p>
</div>
<a class="btn btn-red" style="left:147px;top:1180px;width:214px;height:42px;font-size:13px">Video presentation</a>
<div class="abs media" style="left:575px;top:892px;width:480px;height:336px" role="img" aria-label="Photo of hands typing on a laptop showing a donate screen"></div>
<div class="play" style="left:590px;top:1166px"><i><svg width="12" height="12" viewBox="0 0 12 12"><path d="M3 1l8 5-8 5z" fill="var(--red)"/></svg></i><span>Watch<br>INTRO VIDEO</span></div>

<!-- HOW IT WORKS -->
<div class="abs" style="left:0;top:1337px;width:1200px;height:705px" role="img" aria-label="Blue tinted photo of children behind the section">
  <svg width="1200" height="705" viewBox="0 0 1200 705">
    <defs><linearGradient id="hw" x1="0" y1="0" x2="0" y2="1"><stop offset="0" stop-color="#3a9ad6"/><stop offset="1" stop-color="#2b7fc2"/></linearGradient></defs>
    <polygon points="0,0 1200,0 1200,597 418,703 0,597" fill="url(#hw)"/>
    <polyline points="0,600 418,703 1200,600" fill="none" stroke="var(--navy)" stroke-width="6"/>
  </svg>
</div>
<h2 class="abs how-title">How it works</h2>
<div class="rule" style="left:565px;top:1482px;background:var(--white)"></div>

<div class="step" style="left:145px">
  <div class="ico"><svg width="50" height="50" viewBox="0 0 50 50" fill="none" stroke="#fff" stroke-width="2.5"><rect x="10" y="6" width="26" height="36" rx="2"/><path d="M16 16h14M16 23h14M16 30h9"/><path d="M40 12v28l-3 5-3-5V12z"/></svg></div>
  <h3>NEMO ENIM IPSAM</h3>
  <p>Lorem ipsum dolor sit amet, consectetur adipiscing elit, sed do eiusmod tempor incididunt ut labore et dolore magna aliqua. Ut enim ad minim veniam, quis</p>
</div>
<div class="joint" style="left:418px"><svg width="18" height="18" viewBox="0 0 18 18" fill="none" stroke="var(--blue)" stroke-width="2"><path d="M3 4l5 5-5 5M9 4l5 5-5 5"/></svg></div>
<div class="step" style="left:459px">
  <div class="ico"><svg width="52" height="52" viewBox="0 0 52 52" fill="none" stroke="#fff" stroke-width="2.5"><circle cx="18" cy="14" r="6"/><circle cx="34" cy="14" r="6"/><path d="M8 40v-8a10 10 0 0 1 20 0v8M24 40v-8a10 10 0 0 1 20 0v8"/><circle cx="26" cy="26" r="22"/></svg></div>
  <h3>NEMO ENIM IPSAM</h3>
  <p>Lorem ipsum dolor sit amet, consectetur adipiscing elit, sed do eiusmod tempor incididunt ut labore et dolore magna aliqua. Ut enim ad minim veniam, quis</p>
</div>
<div class="joint" style="left:733px"><svg width="18" height="18" viewBox="0 0 18 18" fill="none" stroke="var(--blue)" stroke-width="2"><path d="M3 4l5 5-5 5M9 4l5 5-5 5"/></svg></div>
<div class="step" style="left:771px">
  <div class="ico"><svg width="52" height="52" viewBox="0 0 52 52" fill="none" stroke="#fff" stroke-width="2.5"><circle cx="28" cy="14" r="7"/><path d="M6 34h10l8 4h10l12-8M16 34v10H6"/><path d="M24 38h10"/></svg></div>
  <h3>NEMO ENIM IPSAM</h3>
  <p>Lorem ipsum dolor sit amet, consectetur adipiscing elit, sed do eiusmod tempor incididunt ut labore et dolore magna aliqua. Ut enim ad minim veniam, quis</p>
</div>

<!-- PROJECTS -->
<h2 class="abs sec-title" style="top:2126px">Projects To Finance</h2>
<div class="rule" style="left:565px;top:2196px"></div>
<p class="abs" style="left:0;width:1200px;top:2228px;text-align:center;font-size:16px;color:#333">You shall finance one project or more.</p>

<div class="cat" style="left:143px;background:var(--orange)"><i><svg width="50" height="50" viewBox="0 0 50 50" fill="none" stroke="var(--orange)" stroke-width="2.5"><circle cx="25" cy="27" r="16"/><path d="M25 11c0-6 6-8 10-8-1 6-4 9-10 8zM12 24c6 0 9 4 9 9M30 40c0-6 4-8 9-9"/></svg></i>ENVIRONMENT</div>
<div class="cat" style="left:371px;background:var(--green)"><i><svg width="50" height="50" viewBox="0 0 50 50" fill="none" stroke="var(--green)" stroke-width="2.5"><path d="M6 42h38M10 42V24l12-10 12 10v18M22 42V32h8v10M30 10l8-6 8 6"/></svg></i>SOCIAL</div>
<div class="cat" style="left:599px;background:var(--health)"><i><svg width="50" height="50" viewBox="0 0 50 50"><rect x="7" y="14" width="36" height="28" rx="4" fill="var(--health)"/><path d="M19 14v-5h12v5" fill="none" stroke="var(--health)" stroke-width="3"/><path d="M25 20v16M17 28h16" stroke="#fff" stroke-width="5"/></svg></i>HEALTH</div>
<div class="cat" style="left:827px;background:var(--edu)"><i><svg width="50" height="50" viewBox="0 0 50 50" fill="none" stroke="var(--edu)" stroke-width="2.5"><circle cx="25" cy="14" r="7"/><path d="M6 24l19 6 19-6v16l-19 6-19-6zM25 30v16"/></svg></i>EDUCATION</div>

<div class="card" style="left:143px;top:2550px"><div class="photo" style="background:linear-gradient(135deg,#6b4a38,#a6744f 50%,#3d2e2a)" role="img" aria-label="Photo of children reaching their hands toward the camera"></div><h3>PROJECT 1</h3><p>Sed ut perspiciatis unde omnis iste natus error sit voluptatem accustium dlorue laudantium, totam rem</p><div class="foot"><span class="view">VIEW DETAILS</span><span class="price">$ 250</span></div></div>
<div class="card" style="left:455px;top:2550px"><div class="photo" style="background:linear-gradient(135deg,#4a3a34,#8a6a52 50%,#c2a24a)" role="img" aria-label="Photo of a group of young children looking up"></div><h3>PROJECT 2</h3><p>Sed ut perspiciatis unde omnis iste natus error sit voluptatem accustium dlorue laudantium, totam rem</p><div class="foot"><span class="view">VIEW DETAILS</span><span class="price">$ 250</span></div></div>
<div class="card" style="left:767px;top:2550px"><div class="photo" style="background:linear-gradient(135deg,#4d7aa8,#b24a4a 50%,#3b4b6a)" role="img" aria-label="Photo of children holding up colourful school backpacks"></div><h3>PROJECT 3</h3><p>Sed ut perspiciatis unde omnis iste natus error sit voluptatem accustium dlorue laudantium, totam rem</p><div class="foot"><span class="view">VIEW DETAILS</span><span class="price">$ 250</span></div></div>

<div class="card" style="left:143px;top:3015px"><div class="photo" style="background:linear-gradient(135deg,#3a2c28,#8a5a3e 50%,#c98a4a)" role="img" aria-label="Photo of children studying at a desk"></div><h3>PROJECT 4</h3><p>Sed ut perspiciatis unde omnis iste natus error sit voluptatem accustium dlorue laudantium, totam rem</p><div class="foot"><span class="view">VIEW DETAILS</span><span class="price">$ 250</span></div></div>
<div class="card" style="left:455px;top:3015px"><div class="photo" style="background:linear-gradient(135deg,#5a3a2c,#b0744c 50%,#d6a26a)" role="img" aria-label="Photo of two laughing children close together"></div><h3>PROJECT 5</h3><p>Sed ut perspiciatis unde omnis iste natus error sit voluptatem accustium dlorue laudantium, totam rem</p><div class="foot"><span class="view">VIEW DETAILS</span><span class="price">$ 250</span></div></div>
<div class="card" style="left:767px;top:3015px"><div class="photo" style="background:linear-gradient(135deg,#4a6a3a,#6a4a3a 50%,#2e2620)" role="img" aria-label="Photo of a group of joyful children outdoors"></div><h3>PROJECT 6</h3><p>Sed ut perspiciatis unde omnis iste natus error sit voluptatem accustium dlorue laudantium, totam rem</p><div class="foot"><span class="view">VIEW DETAILS</span><span class="price">$ 250</span></div></div>

<!-- LATEST NEWS -->
<svg class="abs" style="left:0;top:3555px" width="1200" height="760" viewBox="0 0 1200 760">
  <polygon points="0,88 418,4 1200,88 1200,760 0,760" fill="var(--lavender)"/>
  <polyline points="0,92 418,4 1200,92" fill="none" stroke="var(--navy)" stroke-width="6"/>
</svg>
<h2 class="abs sec-title" style="top:3688px">Latest News</h2>
<div class="rule" style="left:565px;top:3756px"></div>
<div class="search" style="left:145px;top:3817px;width:428px;height:40px;border-radius:2px;font-size:12px;padding:0 18px">Your search goes here...
  <svg width="20" height="20" viewBox="0 0 26 26"><circle cx="11" cy="11" r="8" fill="none" stroke="var(--blue)" stroke-width="3"/><path d="M17 17l7 7" stroke="var(--navy)" stroke-width="3.5" stroke-linecap="round"/></svg>
</div>
<div class="abs media" style="left:145px;top:3876px;width:428px;height:322px;background:linear-gradient(135deg,#8a7a6a,#5a4a42 50%,#b8a28a)" role="img" aria-label="Photo of a girl carrying a baby"></div>
<div class="play" style="left:160px;top:4140px"><i><svg width="12" height="12" viewBox="0 0 12 12"><path d="M3 1l8 5-8 5z" fill="var(--red)"/></svg></i><span>Watch<br>INTRO VIDEO</span></div>

<article class="news" style="top:3819px"><div class="photo" style="background:linear-gradient(135deg,#c8d8e8,#e0c49a 60%,#8a6a4a)" role="img" aria-label="Photo of a child beside a donation box"></div><h4>Nemo enim ipsam volupta</h4><div class="meta"><span>&#9638; Jan 25, 2020</span><span>&#9675; 2 comments</span></div><p>Sed ut perspiciatis unde omnis iste natus error sit vuptatem aum doloremque</p></article>
<article class="news" style="top:4019px"><div class="photo" style="background:linear-gradient(135deg,#6a9a4a,#c4d8a0 50%,#3a7a3a)" role="img" aria-label="Photo of children around a green bucket outdoors"></div><h4>Nemo enim ipsam volupta</h4><div class="meta"><span>&#9638; Jan 25, 2020</span><span>&#9675; 2 comments</span></div><p>Sed ut perspiciatis unde omnis iste natus error sit vuptatem aum doloremque</p></article>

<!-- BECOME PARTNER -->
<section class="abs partners"></section>
<h2 class="abs sec-title" style="top:4378px;color:var(--white)">Become Partner</h2>
<svg class="abs" style="left:92px;top:4562px" width="20" height="36" viewBox="0 0 20 36"><path d="M18 2L2 18l16 16" fill="none" stroke="#8e9bb6" stroke-width="2"/></svg>
<svg class="abs" style="left:1088px;top:4562px" width="20" height="36" viewBox="0 0 20 36"><path d="M2 2l16 16L2 34" fill="none" stroke="#8e9bb6" stroke-width="2"/></svg>
<div class="badge" style="left:149px;top:4492px"><span style="width:100px;height:20px"></span></div>
<div class="badge" style="left:335px;top:4492px"><span style="width:90px;height:26px"></span></div>
<div class="badge" style="left:518px;top:4492px"><span style="width:104px;height:22px"></span></div>
<div class="badge" style="left:702px;top:4492px"><span style="width:70px;height:26px"></span></div>
<div class="badge" style="left:885px;top:4492px"><span style="width:110px;height:26px"></span></div>
<div class="badge" style="left:149px;top:4586px"><span style="width:110px;height:28px"></span></div>
<div class="badge" style="left:335px;top:4586px"><span style="width:92px;height:22px"></span></div>
<div class="badge" style="left:518px;top:4586px"><span style="width:96px;height:20px"></span></div>
<div class="badge" style="left:702px;top:4586px"><span style="width:48px;height:40px;border-radius:50%"></span></div>
<div class="badge" style="left:885px;top:4586px"><span style="width:120px;height:30px"></span></div>
<div class="abs skyline" role="img" aria-label="Illustrated city skyline band"></div>

<!-- FOOTER -->
<h4 class="foot-h" style="left:143px">VELQUOR.ORG</h4>
<p class="foot-p" style="left:143px;top:4932px;width:300px">Nemo enim ipsam voluptatem quia voluptas sit aspernatur aut odit aut fugit, sed quia Nemo enim ipsam voluptatem quia voluptas sit aspernatur aut odit aut fugit, sed quia</p>
<div class="social"><i></i><i></i><i></i><i></i></div>

<h4 class="foot-h" style="left:500px">CONTACT US</h4>
<div class="contact" style="top:4940px"><i><svg width="14" height="18" viewBox="0 0 14 18" fill="none" stroke="#333" stroke-width="1.6"><path d="M7 17s6-6 6-10A6 6 0 0 0 1 7c0 4 6 10 6 10z"/><circle cx="7" cy="7" r="2"/></svg></i><span>velquor.org<br>2210 Alder Street, 4th floor<br>Houston, TX 77002</span></div>
<div class="contact" style="top:5010px"><i><svg width="16" height="16" viewBox="0 0 16 16" fill="none" stroke="#333" stroke-width="1.6"><path d="M3 1h3l1.5 4-2 1.5a9 9 0 0 0 4 4l1.5-2 4 1.5v3a2 2 0 0 1-2 2A13 13 0 0 1 1 3a2 2 0 0 1 2-2z"/></svg></i><span>Call us today:<br>(713) 555-0148</span></div>
<div class="contact" style="top:5064px"><i><svg width="16" height="12" viewBox="0 0 16 12" fill="none" stroke="#333" stroke-width="1.6"><rect x="1" y="1" width="14" height="10"/><path d="M1 1l7 6 7-6"/></svg></i><span>Email :<br>info@velquor.org</span></div>

<h4 class="foot-h" style="left:781px">SIGN UP FOR NEWSLETTER</h4>
<p class="foot-p" style="left:781px;top:4932px;width:280px">Excepteur sint occaecat cupidatat non proident, sunt in culpa qui officia deserunt</p>
<div class="abs" style="left:781px;top:4998px;width:274px;height:38px;border:1px solid #d8d8de;border-radius:20px;font-size:11px;color:#666;padding:11px 16px">Enter email</div>
<a class="btn btn-red" style="left:781px;top:5050px;width:114px;height:36px;font-size:14px;font-weight:500">Sign up</a>

<div class="abs copy">© Copyright 2020 velquor.org. All Rights Reserved.</div>

</body>
</html>
```